Lead Sales Portal Needs to Generate B2B Signup's

We are looking for banner ad designs to drive new business (B2B) traffic to our insurance and mortgage industry self serve lead sites. The sites are HomeLoanProspectHub.com and PolicyProspectHub.com, and we service over 45,000 insurance agents and mortgage lenders in a self serve lead portal model. We want our banners to generate more of these clients.

Our clients come to our sites, browse our database and then pick out and purchase the consumer leads that they need to generate new business.

We advertise extensively on Zorvex and on other PPC platforms, and our existing banners are looking really tired.

Some of the ad copy that works well for us is:

Cherry Pick Your Life Leads - Why Pay More Than $3.50 For Life Insurance Leads?
Sign up today and we'll match up to $250

Agents - Here's $250 For New Clients. Cherry Pick Your Life Insurance Leads & Save! Sign up today and we'll match up to $250

One of our Landing Pages that performs well is here:
http://www.policyprospecthub.com/lp/008/

One of our competitors ad's are here:

http://www.brivlo.com/search/results?q=QuipRate&ad=427360

We're looking for a design that is eye catching, uses our "Deeply Discounted Leads" and our "$250 match bonus"

Target Market(s)

These are insurance agents and mortgage lenders. All of our clients are business' or individuals within the business. This is a B2B campaign,

Industry/Entity Type

Insurance

Requirements
Must have
• We must have the logos for the sites in the banners. Also, we must have a call to action arrow and "Go" button

One or two designs.

File type

.JPEG
.JPG
.PNG
.GIF

File size

150 KB or smaller

Image sizes

Vertical rectangle: 240 x 400
Mobile leaderboard: 320 x 50
Banner: 468 x 60
Leaderboard: 728 x 90
Square: 250 x 250
Small square: 200 x 200
Large rectangle: 336 x 280
Inline rectangle: 300 x 250
Skyscraper: 120 x 600
Wide skyscraper: 160 x 600
Half-page: 300 x 600
Large leaderboard: 970 x 90

```html
<!DOCTYPE html>
<html lang="en">
<head>
<meta charset="utf-8">
<title>Life Insurance Leads Banner Set</title>
<link rel="stylesheet" href="https://fonts.googleapis.com/css2?family=Oswald:wght@400;500&family=Arimo:wght@400;700&display=swap">
<style>
  :root {
    --canvas: #ececec;
    --panel: #1c1c1c;
    --ink: #ffffff;
    --accent: #f6c500;
    --accent-deep: #f0a800;
    --silver: #c9c9c9;
    --rule: #555555;
    --button-ink: #1a1a1a;
    --brand-ink: #e4e4e4;
    --photo: linear-gradient(180deg, #f1efec 0%, #ddd3c8 35%, #b89c86 55%, #3a3a3a 78%, #1e1e1e 100%);
    --photo-side: linear-gradient(90deg, #f1efec 0%, #d8c6b4 40%, #6d5e52 75%, #2a2a2a 100%);
  }
  * { box-sizing: border-box; margin: 0; padding: 0; }
  html, body { width: 1200px; height: 876px; overflow: hidden; }
  body { background: var(--canvas); position: relative; font-family: "Arimo", Arial, sans-serif; color: var(--ink); }

  .banner { position: absolute; overflow: hidden; background: var(--panel); }
  .photo { position: absolute; inset: 0; background: var(--photo); }
  .banner--side .photo, .banner--strip .photo { background: var(--photo-side); }

  .panel { position: absolute; background: var(--panel); display: flex; flex-direction: column; align-items: center; text-align: center; }
  .rule { position: absolute; overflow: visible; }

  .headline { font-family: "Oswald", "Arial Narrow", sans-serif; font-weight: 500; text-transform: uppercase; line-height: 1.08; letter-spacing: -0.3px; white-space: nowrap; }
  .headline .hl { color: var(--accent); }
  .offer { font-family: "Oswald", "Arial Narrow", sans-serif; font-weight: 500; text-transform: uppercase; line-height: 1.1; letter-spacing: -0.3px; white-space: nowrap; }
  .offer .hl { color: var(--accent); }
  .divider { height: 1px; background: var(--rule); }

  .perks { list-style: none; text-align: left; line-height: 1.3; }
  .perks li { display: flex; align-items: center; gap: 0.3em; white-space: nowrap; }
  .perks svg { width: 0.95em; height: 0.95em; flex: none; }

  .go { display: inline-flex; align-items: center; gap: 0.35em; background: linear-gradient(180deg, var(--accent) 0%, var(--accent-deep) 100%); color: var(--button-ink); font-family: "Oswald", "Arial Narrow", sans-serif; font-weight: 500; border-radius: 3px; padding: 0.15em 0.35em 0.15em 0.5em; line-height: 1.2; box-shadow: 0 1px 2px rgba(0,0,0,.5); }
  .go svg { width: 1.05em; height: 1.05em; }

  .brand { display: inline-flex; align-items: center; gap: 0.35em; color: var(--brand-ink); white-space: nowrap; }
  .brand-dot { width: 1.3em; height: 1.3em; border-radius: 50%; background: #8d8d8d; flex: none; }

  /* Wide skyscraper 160x600 */
  .sky { left: 28px; top: 37px; width: 167px; height: 626px; }
  .sky .photo { height: 300px; }
  .sky .panel { top: 258px; left: 0; right: 0; bottom: 0; clip-path: polygon(0 18px, 50% 0, 100% 18px, 100% 100%, 0 100%); padding-top: 34px; }
  .sky .rule { top: 250px; left: 0; width: 167px; height: 26px; }
  .sky .headline { font-size: 24px; }
  .sky .headline .big { font-size: 33px; display: block; }
  .sky .divider { width: 140px; margin: 10px 0 10px; }
  .sky .offer { font-size: 19px; }
  .sky .offer .big { font-size: 30px; display: block; }
  .sky .perks { font-size: 12px; margin-top: 6px; }
  .sky .go { font-size: 19px; margin-top: 22px; }
  .sky .brand { font-size: 10px; margin-top: 18px; }

  /* Half-page 300x600 */
  .half { left: 205px; top: 37px; width: 313px; height: 626px; }
  .half .photo { height: 320px; }
  .half .panel { top: 287px; left: 0; right: 0; bottom: 0; clip-path: polygon(0 32px, 50% 0, 100% 22px, 100% 100%, 0 100%); padding-top: 42px; }
  .half .rule { top: 279px; left: 0; width: 313px; height: 44px; }
  .half .headline { font-size: 27px; }
  .half .divider { width: 250px; margin: 12px 0 10px; }
  .half .offer { font-size: 25px; }
  .half .offer .big { font-size: 39px; display: block; }
  .half .perks { font-size: 17px; margin-top: 10px; }
  .half .footer { position: absolute; left: 12px; right: 12px; bottom: 14px; display: flex; justify-content: space-between; align-items: center; }
  .half .brand { font-size: 13.5px; }
  .half .go { font-size: 21px; }

  /* Vertical rectangle 240x400 */
  .vert { left: 538px; top: 37px; width: 251px; height: 418px; }
  .vert .photo { height: 215px; }
  .vert .panel { top: 190px; left: 0; right: 0; bottom: 0; clip-path: polygon(0 18px, 40% 0, 100% 10px, 100% 100%, 0 100%); padding-top: 28px; }
  .vert .rule { top: 182px; left: 0; width: 251px; height: 28px; }
  .vert .headline { font-size: 20.5px; }
  .vert .offer { font-size: 21px; margin-top: 10px; }
  .vert .perks { font-size: 13px; margin-top: 6px; }
  .vert .footer { position: absolute; left: 8px; right: 10px; bottom: 10px; display: flex; justify-content: space-between; align-items: center; }
  .vert .brand { font-size: 10.5px; }
  .vert .go { font-size: 16px; }

  /* Side-panel squares */
  .side-panel { top: 0; left: 0; bottom: 0; align-items: flex-start; text-align: left; padding: 10px 0 0 11px; }
  .large { left: 811px; top: 37px; width: 351px; height: 292px; }
  .large .panel { width: 178px; clip-path: polygon(0 0, 157px 0, 178px 50%, 157px 100%, 0 100%); }
  .large .rule { left: 150px; top: 0; width: 36px; height: 292px; }
  .large .headline { font-size: 23.5px; }
  .large .headline .big { font-size: 30px; display: block; }
  .large .divider { width: 140px; margin: 8px 0 8px; }
  .large .offer { font-size: 18.5px; }
  .large .offer .big { font-size: 29px; display: block; }
  .large .perks { font-size: 11.5px; margin-top: 4px; }
  .large .brand { position: absolute; left: 6px; bottom: 26px; font-size: 10.5px; }
  .large .go { position: absolute; left: 226px; bottom: 28px; font-size: 19px; }

  .inline { left: 830px; top: 350px; width: 313px; height: 261px; }
  .inline .panel { width: 156px; clip-path: polygon(0 0, 137px 0, 156px 50%, 137px 100%, 0 100%); padding-top: 8px; padding-left: 10px; }
  .inline .rule { left: 130px; top: 0; width: 34px; height: 261px; }
  .inline .headline { font-size: 21px; }
  .inline .headline .big { font-size: 27px; display: block; }
  .inline .divider { width: 124px; margin: 7px 0 7px; }
  .inline .offer { font-size: 17px; }
  .inline .offer .big { font-size: 26px; display: block; }
  .inline .perks { font-size: 10.5px; margin-top: 3px; }
  .inline .brand { position: absolute; left: 6px; bottom: 16px; font-size: 9.5px; }
  .inline .go { position: absolute; left: 200px; bottom: 24px; font-size: 18px; }

  /* Strip banners */
  .strip-panel { top: 0; bottom: 0; right: 0; flex-direction: row; align-items: center; text-align: left; }
  .strip-panel .headline .big { display: block; }
  .strip-panel .cta-block { margin-left: auto; display: flex; flex-direction: column; align-items: flex-end; }

  .banner468 { left: 28px; top: 681px; width: 489px; height: 61px; }
  .banner468 .photo { width: 140px; }
  .banner468 .panel { left: 0; clip-path: polygon(112px 0, 100% 0, 100% 100%, 112px 100%, 132px 50%); padding-left: 145px; padding-right: 6px; }
  .banner468 .rule { left: 106px; top: 0; width: 32px; height: 61px; }
  .banner468 .headline { font-size: 12px; }
  .banner468 .headline .big { font-size: 18px; line-height: 1; }
  .banner468 .match-block { margin-left: 16px; }
  .banner468 .offer { font-size: 10.5px; }
  .banner468 .perks { font-size: 8px; margin-top: 1px; }
  .banner468 .cta-block { gap: 8px; }
  .banner468 .brand { font-size: 7.5px; }
  .banner468 .go { font-size: 11px; margin-right: 28px; }

  .leader { left: 28px; top: 756px; width: 761px; height: 93px; }
  .leader .photo { width: 235px; }
  .leader .panel { left: 0; clip-path: polygon(207px 0, 100% 0, 100% 100%, 207px 100%, 232px 50%); padding-left: 229px; padding-right: 12px; }
  .leader .rule { left: 200px; top: 0; width: 38px; height: 93px; }
  .leader .headline { font-size: 20px; }
  .leader .headline .big { font-size: 28px; line-height: 1; }
  .leader .match-block { margin-left: 30px; }
  .leader .offer { font-size: 18px; }
  .leader .perks { font-size: 13px; margin-top: 3px; }
  .leader .cta-block { gap: 10px; }
  .leader .brand { font-size: 12px; }
  .leader .go { font-size: 20px; margin-right: 10px; }
</style>
</head>
<body>

<svg width="0" height="0" style="position:absolute">
  <defs>
    <symbol id="tick" viewBox="0 0 16 16"><path d="M2 8.5 L6 13 L14 2.5" fill="none" stroke="#f6c500" stroke-width="2.6" stroke-linecap="round" stroke-linejoin="round"/></symbol>
    <symbol id="arrow" viewBox="0 0 20 20"><circle cx="10" cy="10" r="9.5" fill="#1e1e1e"/><path d="M8 5.5 L12.5 10 L8 14.5" fill="none" stroke="#ffffff" stroke-width="2.6" stroke-linecap="round" stroke-linejoin="round"/></symbol>
  </defs>
</svg>

<!-- Wide skyscraper -->
<section class="banner sky">
  <div class="photo" role="img" aria-label="Photo of a smiling businessman and businesswoman in dark suits"></div>
  <svg class="rule" viewBox="0 0 167 26" preserveAspectRatio="none"><polyline points="0,26 83.5,8 167,26" fill="none" stroke="var(--silver)" stroke-width="6"/></svg>
  <div class="panel">
    <p class="headline">Pick your life<span class="big hl">Insurance</span>Leads &amp; save!</p>
    <div class="divider"></div>
    <p class="offer">We'll match<span class="big hl">Up to $250</span></p>
    <ul class="perks">
      <li><svg><use href="#tick"/></svg>Starting at $6.00 / lead.</li>
      <li><svg><use href="#tick"/></svg>No Minimums.</li>
      <li><svg><use href="#tick"/></svg>Deeply discounted leads.</li>
    </ul>
    <span class="go">GO<svg><use href="#arrow"/></svg></span>
    <span class="brand"><span class="brand-dot"></span>Home Loan Prospect Hub</span>
  </div>
</section>

<!-- Half-page -->
<section class="banner half">
  <div class="photo" role="img" aria-label="Photo of a smiling businessman and businesswoman in dark suits"></div>
  <svg class="rule" viewBox="0 0 313 44" preserveAspectRatio="none"><polyline points="0,42 156.5,10 313,32" fill="none" stroke="var(--silver)" stroke-width="6"/></svg>
  <div class="panel">
    <p class="headline">Pick your life<br><span class="hl">Insurance leads &amp; save!</span></p>
    <div class="divider"></div>
    <p class="offer">We'll match<span class="big hl">Up to $250</span></p>
    <ul class="perks">
      <li><svg><use href="#tick"/></svg>Starting at $6.00 / lead.</li>
      <li><svg><use href="#tick"/></svg>No Minimums.</li>
      <li><svg><use href="#tick"/></svg>Deeply discounted leads.</li>
    </ul>
    <div class="footer">
      <span class="brand"><span class="brand-dot"></span>Home Loan Prospect Hub</span>
      <span class="go">GO<svg><use href="#arrow"/></svg></span>
    </div>
  </div>
</section>

<!-- Vertical rectangle -->
<section class="banner vert">
  <div class="photo" role="img" aria-label="Photo of a smiling businessman and businesswoman in dark suits"></div>
  <svg class="rule" viewBox="0 0 251 28" preserveAspectRatio="none"><polyline points="0,26 100.4,8 251,18" fill="none" stroke="var(--silver)" stroke-width="6"/></svg>
  <div class="panel">
    <p class="headline">Pick your life<br><span class="hl">Insurance leads &amp; save!</span></p>
    <p class="offer">We'll match <span class="hl">Up to $250</span></p>
    <ul class="perks">
      <li><svg><use href="#tick"/></svg>Starting at $6.00 / lead.</li>
      <li><svg><use href="#tick"/></svg>No Minimums.</li>
      <li><svg><use href="#tick"/></svg>Deeply discounted leads.</li>
    </ul>
    <div class="footer">
      <span class="brand"><span class="brand-dot"></span>Home Loan Prospect Hub</span>
      <span class="go">GO<svg><use href="#arrow"/></svg></span>
    </div>
  </div>
</section>

<!-- Large rectangle -->
<section class="banner banner--side large">
  <div class="photo" role="img" aria-label="Photo of a smiling businessman and businesswoman in dark suits"></div>
  <svg class="rule" viewBox="0 0 36 292" preserveAspectRatio="none"><polyline points="10,0 31,146 10,292" fill="none" stroke="var(--silver)" stroke-width="6"/></svg>
  <div class="panel side-panel">
    <p class="headline">Pick your life<span class="big hl">Insurance</span>Leads &amp; save!</p>
    <div class="divider"></div>
    <p class="offer">We'll match<span class="big hl">Up to $250</span></p>
    <ul class="perks">
      <li><svg><use href="#tick"/></svg>Starting at $6.00 / lead.</li>
      <li><svg><use href="#tick"/></svg>No Minimums.</li>
      <li><svg><use href="#tick"/></svg>Deeply discounted leads.</li>
    </ul>
    <span class="brand"><span class="brand-dot"></span>Home Loan Prospect Hub</span>
  </div>
  <span class="go">GO<svg><use href="#arrow"/></svg></span>
</section>

<!-- Inline rectangle -->
<section class="banner banner--side inline">
  <div class="photo" role="img" aria-label="Photo of a smiling businessman and businesswoman in dark suits"></div>
  <svg class="rule" viewBox="0 0 34 261" preserveAspectRatio="none"><polyline points="9,0 28,130.5 9,261" fill="none" stroke="var(--silver)" stroke-width="6"/></svg>
  <div class="panel side-panel">
    <p class="headline">Pick your life<span class="big hl">Insurance</span>Leads &amp; save!</p>
    <div class="divider"></div>
    <p class="offer">We'll match<span class="big hl">Up to $250</span></p>
    <ul class="perks">
      <li><svg><use href="#tick"/></svg>Starting at $6.00 / lead.</li>
      <li><svg><use href="#tick"/></svg>No Minimums.</li>
      <li><svg><use href="#tick"/></svg>Deeply discounted leads.</li>
    </ul>
    <span class="brand"><span class="brand-dot"></span>Home Loan Prospect Hub</span>
  </div>
  <span class="go">GO<svg><use href="#arrow"/></svg></span>
</section>

<!-- Banner 468 -->
<section class="banner banner--strip banner468">
  <div class="photo" role="img" aria-label="Photo of a smiling businessman and businesswoman"></div>
  <svg class="rule" viewBox="0 0 32 61" preserveAspectRatio="none"><polyline points="6,0 26,30.5 6,61" fill="none" stroke="var(--silver)" stroke-width="4"/></svg>
  <div class="panel strip-panel">
    <p class="headline">Pick your life<span class="big hl">Insurance</span>Leads &amp; save!</p>
    <div class="match-block">
      <p class="offer">We'll match <span class="hl">Up to $250</span></p>
      <ul class="perks">
        <li><svg><use href="#tick"/></svg>Starting at $6.00 / lead.</li>
        <li><svg><use href="#tick"/></svg>No Minimums.</li>
        <li><svg><use href="#tick"/></svg>Deeply discounted leads.</li>
      </ul>
    </div>
    <div class="cta-block">
      <span class="brand"><span class="brand-dot"></span>Home Loan Prospect Hub</span>
      <span class="go">GO<svg><use href="#arrow"/></svg></span>
    </div>
  </div>
</section>

<!-- Large leaderboard -->
<section class="banner banner--strip leader">
  <div class="photo" role="img" aria-label="Photo of a smiling businessman and businesswoman"></div>
  <svg class="rule" viewBox="0 0 38 93" preserveAspectRatio="none"><polyline points="7,0 32,46.5 7,93" fill="none" stroke="var(--silver)" stroke-width="6"/></svg>
  <div class="panel strip-panel">
    <p class="headline">Pick your life<span class="big hl">Insurance</span>Leads &amp; save!</p>
    <div class="match-block">
      <p class="offer">We'll match <span class="hl">Up to $250</span></p>
      <ul class="perks">
        <li><svg><use href="#tick"/></svg>Starting at $6.00 / lead.</li>
        <li><svg><use href="#tick"/></svg>No Minimums.</li>
        <li><svg><use href="#tick"/></svg>Deeply discounted leads.</li>
      </ul>
    </div>
    <div class="cta-block">
      <span class="brand"><span class="brand-dot"></span>Home Loan Prospect Hub</span>
      <span class="go">GO<svg><use href="#arrow"/></svg></span>
    </div>
  </div>
</section>

</body>
</html>
```